Nestlyo Business Card Project showing the logo and a vonka image on the rear

Design a whacky but professional business card, the logo is for the front and the Vonka image is for the rear. Happy to consider other open source Vonka Images if the designer wants to select one from the web. Nestlyo is a competitor to KPX.com.au and Plotfield.com.au and is based around every property in Australia

Business

Name, Title, Email, Web, Phone Number

• avenir

• Image on Back logo on front
• Happy to consider other images on rear, preftably Oscar Vonka. Image supplied I own, we can use open source other Vonka Images

```html
<!DOCTYPE html>
<html lang="en">
<head>
<meta charset="UTF-8">
<title>Nestlyo Business Card</title>
<link rel="stylesheet" href="https://fonts.googleapis.com/css2?family=Mulish:wght@400;600;800&display=swap">
<style>
  :root {
    --backdrop: #e3e4e6;
    --card-white: #ffffff;
    --ink: #111111;
    --accent: #f7931e;
    --divider: #222222;
    --art-light: #5f8fd0;
    --art-deep: #27409a;
  }
  * { box-sizing: border-box; margin: 0; padding: 0; }
  html, body {
    width: 1200px;
    height: 800px;
    overflow: hidden;
  }
  body {
    background: var(--backdrop);
    font-family: "Mulish", sans-serif;
    display: flex;
    align-items: center;
    justify-content: center;
    gap: 60px;
  }
  .card {
    width: 500px;
    height: 286px;
    border-radius: 4px;
    box-shadow: 0 10px 24px rgba(0, 0, 0, 0.12);
    overflow: hidden;
    flex: none;
  }
  .card-rear {
    background: linear-gradient(135deg, var(--art-light) 0%, var(--art-deep) 100%);
  }
  .card-front {
    background: var(--card-white);
    display: flex;
    align-items: center;
    padding: 0 34px 0 44px;
  }
  .brand {
    display: flex;
    align-items: center;
    gap: 10px;
    flex: none;
  }
  .brand-square {
    width: 26px;
    height: 26px;
    background: var(--accent);
  }
  .brand-name {
    font-weight: 800;
    font-size: 40px;
    color: var(--ink);
    letter-spacing: 0.5px;
  }
  .divider {
    width: 1.5px;
    height: 96px;
    background: var(--divider);
    margin: 0 24px 0 26px;
    flex: none;
  }
  .contact {
    display: flex;
    flex-direction: column;
    gap: 3px;
  }
  .person-name {
    font-weight: 800;
    font-size: 20px;
    color: var(--ink);
  }
  .person-title {
    font-weight: 600;
    font-size: 15px;
    color: var(--accent);
    margin-bottom: 4px;
  }
  .contact-line {
    display: flex;
    align-items: center;
    gap: 7px;
    font-size: 13px;
    color: var(--ink);
    white-space: nowrap;
  }
  .contact-line svg {
    width: 11px;
    height: 11px;
    flex: none;
  }
</style>
</head>
<body>
  <div class="card card-rear" role="img" aria-label="Rear artwork: colourful cartoon city skyline illustration"></div>

  <div class="card card-front">
    <div class="brand">
      <span class="brand-square"></span>
      <span class="brand-name">Nestlyo</span>
    </div>
    <span class="divider"></span>
    <div class="contact">
      <span class="person-name">Daniel Marsh</span>
      <span class="person-title">CEO/Founder</span>
      <span class="contact-line">
        <svg viewBox="0 0 12 12" aria-hidden="true"><path d="M2.5 1 L4.5 1 L5.3 3.6 L4 4.6 Q5 7 7.4 8 L8.4 6.7 L11 7.5 L11 9.5 Q10.5 11 9 11 Q1 10 1 3 Q1 1.5 2.5 1 Z" fill="var(--accent)"/></svg>
        555-014-2630
      </span>
      <span class="contact-line">
        <svg viewBox="0 0 12 12" aria-hidden="true"><rect x="0.5" y="2" width="11" height="8" rx="1" fill="var(--accent)"/><path d="M1 2.6 L6 6.6 L11 2.6" stroke="#fff" stroke-width="1" fill="none"/></svg>
        Daniel@Nestlyo.com
      </span>
      <span class="contact-line">
        <svg viewBox="0 0 12 12" aria-hidden="true"><circle cx="6" cy="6" r="5.5" fill="var(--accent)"/><path d="M0.8 6 H11.2 M6 0.8 Q3 6 6 11.2 M6 0.8 Q9 6 6 11.2" stroke="#fff" stroke-width="0.8" fill="none"/></svg>
        www.nestlyohomes.com
      </span>
    </div>
  </div>
</body>
</html>
```